Create a Brochure Design for Harlow Senior Living

Harlow Senior Living is a subsidiary of the Harlow Care Group. This brochure is specifically for the Harlow Senior Living company and brand. Create a 3 panel, front and back, tri-fold brochure. This brochure will be a way to introduce our senior living care home to the community, prospective, clients, and various referral partners. It is modern and state of the art home. Like the home, the brochure must be eye catching, unique in its deliverables (as it doesn’t feel like a care facility) and demonstrate both attention to detail and comfort. Our organization is sophisticated and built around warmth, care and individualized personal attention. The most important aspect of this design is to focus on creating a nurturing, warm, and inviting feel where you would want to put your own loved ones in our care home.
I am open to the creativity of the designer to develop something based on the above criteria; however I would like the design to work well with the existing collateral material. What I mean by that is that while I want everything to have its own personality and stand out as its own brand representative, I still need to be able to tell that the overall design concept stays stylistically inside of the same ‘family’ of existing designed material. Because of this, below I would like for the designer to pull inspiration from the link to our website (Located below) as well as from the attachment of our recently refreshed business cards (Attached). This should allow each design to be unique and creative, while still staying inside of a framework and the feel/style that I am looking for.
Finally, I want all the designers to understand that this brochure design is for a facility where we are responsible to provide care for active, positive, and happy seniors/elders. We have care professionals and staff on-site to provide 24x7, around the clock, care to the elders and geriatric residents as it is needed and required. The photos that are used must represent aging gracefully and with elegance.
Target Market(s)
Seniors(50+), Caring Family Members, Social Workers, Physicians, Hospitals
Industry/Entity Type
Business
Requirements
Must have
- • The company logo must be included.
Nice to have
- Attached you will find a sampling of images related to the long term care industry. Please feel free to use your own images as you see fit. The interior care home pictures are of our actual facility and should be incorporated into the brochure and your design.
Company Information
• Look under the Harlow Senior Living tab at
www.harlowcaregroup.example.

```html
<!DOCTYPE html>
<html lang="en">
<head>
<meta charset="utf-8">
<title>Harlow Senior Living – Tri-fold Brochure</title>
<link href="https://fonts.googleapis.com/css2?family=Open+Sans:ital,wght@0,300;0,400;0,600;0,800;1,300&display=swap" rel="stylesheet">
<style>
  :root {
    --backdrop: #8c8c8c;
    --paper: #ffffff;
    --paper-shade: #f1f1ef;
    --teal: #519693;
    --teal-deep: #3b6d6a;
    --ink: #3a3a3a;
    --ink-soft: #5c5c5c;
    --on-teal: #eef6f5;
  }
  * { box-sizing: border-box; margin: 0; padding: 0; }
  html, body { width: 1200px; height: 817px; overflow: hidden; }
  body {
    background: linear-gradient(160deg, #b3b3b3 0%, var(--backdrop) 55%, #5a5a5a 100%);
    font-family: "Open Sans", Arial, sans-serif;
    color: var(--ink);
  }
  .brochure {
    position: absolute; left: 90px; top: 28px;
    width: 1020px; height: 760px;
    display: flex;
    box-shadow: 0 18px 40px rgba(0,0,0,.35);
  }
  .panel {
    position: relative; width: 340px; height: 760px;
    background: var(--paper); overflow: hidden;
  }
  .panel + .panel { border-left: 1px solid #e3e3e3; }
  .band { position: absolute; left: 0; bottom: 0; width: 340px; height: 240px; }
  .band svg { position: absolute; inset: 0; }

  /* Back flap */
  .quote {
    position: absolute; left: 150px; top: 56px; width: 160px;
    font-weight: 300; font-size: 21px; line-height: 1.3; color: var(--ink-soft);
  }
  .suitcase-photo {
    position: absolute; left: 56px; top: 200px; width: 170px; height: 120px;
    background: linear-gradient(180deg, #7a6a58 0%, #4e3f31 100%);
    border-radius: 10px;
  }
  .web {
    position: absolute; left: 0; width: 340px; top: 400px;
    text-align: center; font-size: 13px; color: var(--ink);
  }
  .neighbors {
    position: absolute; left: 40px; right: 40px; bottom: 90px;
    text-align: center; font-weight: 300; font-style: italic;
    font-size: 17px; line-height: 1.4; color: var(--on-teal);
  }

  /* Brand mark */
  .brand {
    display: flex; align-items: center; gap: 10px;
    color: var(--teal-deep); font-weight: 400;
  }
  .brand-square { background: var(--teal); border-radius: 6px; flex: none; }

  /* Middle panel */
  .middle .brand {
    position: absolute; top: 200px; left: 0; width: 340px;
    justify-content: center; font-size: 22px;
  }
  .middle .brand-square { width: 30px; height: 30px; }
  .contacts {
    position: absolute; left: 0; width: 340px; bottom: 60px;
    text-align: center; color: var(--on-teal);
  }
  .contacts h2 { font-weight: 300; font-size: 26px; letter-spacing: 1px; margin-bottom: 10px; }
  .contacts p { font-size: 12px; line-height: 1.6; }

  /* Cover */
  .cover { background: linear-gradient(180deg, #ecebe8 0%, #fbf8f2 100%); }
  .cover .brand {
    position: absolute; top: 96px; left: 0; width: 340px;
    justify-content: center; font-size: 28px; line-height: 1.1;
  }
  .cover .brand-square { width: 44px; height: 44px; }
  .cover-photo {
    position: absolute; left: 0; top: 210px; width: 340px; height: 360px;
    background: linear-gradient(135deg, #f3e6d6 0%, #d9b79c 40%, #5e6f8e 75%, #e9e0cc 100%);
  }
  .welcome {
    position: absolute; left: 0; bottom: 0; width: 340px; height: 220px;
    background: linear-gradient(180deg, var(--teal-deep) 0%, var(--teal) 100%);
    padding: 40px 0 0 38px; color: #d9d9d9;
  }
  .welcome .light { display: block; font-weight: 300; font-size: 56px; letter-spacing: 2px; line-height: 1; }
  .welcome .bold { display: block; font-weight: 800; font-size: 60px; color: #ffffff; line-height: 1.05; }
</style>
</head>
<body>
  <main class="brochure">
    <section class="panel back-flap">
      <p class="quote">“Just bring your suitcase. We’ll take care for the rest.”</p>
      <div class="suitcase-photo" role="img" aria-label="Photo of a vintage brown leather suitcase"></div>
      <p class="web">www.harlowcaregroup.example</p>
      <div class="band">
        <svg width="340" height="240" viewBox="0 0 340 240" aria-hidden="true">
          <path d="M0 40 Q170 0 340 40 L340 240 L0 240 Z" fill="var(--teal)"/>
        </svg>
        <p class="neighbors">“Neighbors” live at our home—Not “residents”, not “patients”—we’re neighbors!</p>
      </div>
    </section>

    <section class="panel middle">
      <div class="brand"><span class="brand-square"></span><span>Harlow Senior Living</span></div>
      <div class="band">
        <svg width="340" height="240" viewBox="0 0 340 240" aria-hidden="true">
          <path d="M0 40 Q170 0 340 40 L340 240 L0 240 Z" fill="var(--teal)"/>
        </svg>
        <div class="contacts">
          <h2>CONTACTS</h2>
          <p>Harlow Senior Living is located at:<br>
          42 Orchard Lane, Maple Bay, OR 97012<br>
          Tel: 555-014-2286, Fax: 555-014-2297<br>
          E-mail us at info@harlowcare.example</p>
        </div>
      </div>
    </section>

    <section class="panel cover">
      <div class="brand"><span class="brand-square"></span><span>Harlow Senior Living</span></div>
      <div class="cover-photo" role="img" aria-label="Photo of a smiling elderly woman embraced by her adult daughter"></div>
      <h1 class="welcome"><span class="light">WELCOME</span><span class="bold">HOME</span></h1>
    </section>
  </main>
</body>
</html>
```